Professional/modern business card design for construction company

We need a new business card design, double sided keeping it modern, sleek, professional and simple. We are an earthmoving business but do not want any pictures of machinery. I would like one side to have the logo and the other to have all the information, keeping with the colors in our logo. The business card will need to be able to be customised so we can use it for several different managers., we would also like to be able to use the design to apply it to other stationary ie. letterheads, notebooks etc. We do not really have a tag line but we could put on there that we specialise in - Agriculture, Civil Construction and Mining.

Contact Information for Business Card

Brolga Ridge Excavations Pty Ltd
ABN 58 402 937 615
82 Gumleaf Creek Road, Moree NSW 2400

Harold Benton
Managing Director
P 0418 639 204
E haroldbenton@brolgaridgeexc.com.au

Font styles to use
Serif
Sans Serif

Requirements
Nice to have
• I have attached some examples of ideas.
Should not have
• images of machinery

```html
<!DOCTYPE html>
<html lang="en">
<head>
<meta charset="utf-8">
<title>Brolga Ridge Excavations – Business Card</title>
<link href="https://fonts.googleapis.com/css2?family=Roboto:wght@400;500;700&display=swap" rel="stylesheet">
<style>
  :root {
    --charcoal: #3d3d3f;
    --charcoal-light: #4a4a4c;
    --orange: #f08a1c;
    --white: #ffffff;
    --backdrop: #b9b9bb;
  }
  * { box-sizing: border-box; margin: 0; padding: 0; }
  html, body { width: 1200px; height: 930px; overflow: hidden; }
  body {
    background: var(--backdrop);
    font-family: 'Roboto', Arial, sans-serif;
    position: relative;
  }
  .card {
    position: absolute;
    width: 560px;
    height: 320px;
    border-radius: 22px;
    overflow: hidden;
    background: linear-gradient(135deg, var(--charcoal-light), var(--charcoal));
  }
  .card--front { left: 90px; top: 110px; }
  .card--back  { left: 550px; top: 500px; }

  .brand-name {
    position: absolute;
    font-weight: 700;
    font-size: 26px;
    line-height: 1.2;
    letter-spacing: 0.5px;
    text-transform: uppercase;
  }
  .card--front .brand-name {
    color: var(--white);
    left: 0; right: 0; top: 50%;
    transform: translateY(-50%);
    text-align: center;
  }
  .card--back .brand-name {
    color: var(--charcoal);
    right: 34px; top: 46px;
    width: 300px;
    text-align: right;
    font-size: 24px;
  }
  .back-shape { position: absolute; inset: 0; }

  .contact {
    position: absolute;
    left: 30px; bottom: 26px;
    color: var(--white);
    font-size: 12.5px;
    line-height: 1.45;
  }
  .contact__name {
    color: var(--orange);
    font-size: 22px;
    font-weight: 500;
    text-transform: uppercase;
    line-height: 1.1;
  }
  .contact__role { margin-bottom: 8px; }
  .contact__block { margin-bottom: 8px; }
  .contact__row { display: flex; align-items: center; gap: 8px; }
  .contact__row svg { width: 11px; height: 11px; flex: none; }
</style>
</head>
<body>
  <section class="card card--front">
    <p class="brand-name">Brolga Ridge Excavations Pty Ltd</p>
  </section>

  <section class="card card--back">
    <svg class="back-shape" viewBox="0 0 560 320" preserveAspectRatio="none" aria-hidden="true">
      <path d="M200 0 C 240 150, 380 230, 560 220 L560 0 Z" fill="var(--white)"/>
      <path d="M194 0 C 236 156, 380 238, 560 226" fill="none" stroke="var(--orange)" stroke-width="4"/>
    </svg>
    <p class="brand-name">Brolga Ridge Excavations Pty Ltd</p>

    <div class="contact">
      <p class="contact__name">Harold Benton</p>
      <p class="contact__role">Managing Director</p>
      <p class="contact__block">ABN 58 402 937 615</p>
      <p class="contact__block">82 Gumleaf Creek Road,<br>Moree NSW 2400</p>
      <p class="contact__row">
        <svg viewBox="0 0 24 24"><path fill="var(--orange)" d="M6.6 10.8a15 15 0 0 0 6.6 6.6l2.2-2.2c.3-.3.7-.4 1-.2 1.1.4 2.3.6 3.6.6.6 0 1 .4 1 1V20c0 .6-.4 1-1 1A17 17 0 0 1 3 4c0-.6.4-1 1-1h3.5c.6 0 1 .4 1 1 0 1.3.2 2.5.6 3.6.1.3 0 .7-.2 1z"/></svg>
        0418 639 204
      </p>
      <p class="contact__row">
        <svg viewBox="0 0 24 24"><rect x="2" y="5" width="20" height="14" rx="1" fill="none" stroke="var(--orange)" stroke-width="2"/><path d="M2 6l10 7 10-7" fill="none" stroke="var(--orange)" stroke-width="2"/></svg>
        haroldbenton@brolgaridgeexc.com.au
      </p>
      <p class="contact__row">
        <svg viewBox="0 0 24 24"><circle cx="12" cy="12" r="10" fill="none" stroke="var(--orange)" stroke-width="2"/><path d="M2 12h20M12 2c3 3 3 17 0 20M12 2c-3 3-3 17 0 20" fill="none" stroke="var(--orange)" stroke-width="1.6"/></svg>
        www.brolgaridgeexcavations.com
      </p>
    </div>
  </section>
</body>
</html>
```